Flyer-Design für Ferienhausvermietung
Zielgruppe
Wir haben ein Ferienhaus zu vermieten.
Hauptzielgruppe sind hierbei:
Wanderer/Radfahrer
ältere Personen
gebildet
gerne mit Hund
Aufgabenstellung
Es soll ein Flyer im Format DIN A4 erstellt werden.
Der beidseitig bedruckt wird und dann 6seitig gefaltet wird.
Ich benötige für den Flyer:
Beschreibung/Ausstattung des Ferienhauses
Beschreibung der Lage
Beschreibung der Umgebung
Anfahrt/Lage/Kontakt

```html
<!DOCTYPE html>
<html lang="de">
<head>
<meta charset="utf-8">
<title>Ferienhaus – Faltflyer</title>
<link href="https://fonts.googleapis.com/css2?family=Cinzel:wght@700&family=Open+Sans:wght@400;600;700&display=swap" rel="stylesheet">
<style>
  :root{
    --green-dark:#11681f;
    --green-mid:#2f8a1a;
    --lime:#93b818;
    --lime-light:#b8cf4a;
    --pale:#d7e2a2;
    --paper:#e9e9e9;
    --ink:#1f2a12;
    --photo-sky:#a9c9e6;
    --photo-field:#7fa53a;
    --photo-autumn:#c98e2a;
    --photo-room:#b9aa98;
    --photo-wood:#7a5a44;
  }
  *{box-sizing:border-box;margin:0;padding:0}
  html,body{width:1200px;height:900px;overflow:hidden;background:var(--paper)}
  body{font-family:"Open Sans",Arial,sans-serif;color:var(--ink);position:relative}
  .sheet{position:absolute;top:241px;width:585px;height:418px;display:flex;box-shadow:0 6px 18px rgba(0,0,0,.18);overflow:hidden}
  .sheet--outside{left:10px}
  .sheet--inside{left:605px}
  .panel{position:relative;width:195px;height:100%;overflow:hidden}
  .photo{position:absolute}
  .photo--landscape{background:linear-gradient(180deg,var(--photo-sky) 0%,#d8e6ef 18%,var(--photo-autumn) 30%,var(--photo-field) 55%,#5f8f2a 100%)}
  .photo--village{background:linear-gradient(160deg,var(--photo-autumn) 0%,var(--photo-field) 45%,#4f7f26 100%)}
  .photo--room{background:linear-gradient(170deg,#f2efe9 0%,var(--photo-room) 60%,var(--photo-wood) 100%)}
  .photo--bath{background:linear-gradient(170deg,#e8e4de 0%,#a99e92 70%,#6d5b4b 100%)}
  .framed{border:2px solid #fff}
  .caption{position:absolute;font-size:8px;font-weight:700;text-align:center;width:100%}

  /* outside */
  .contact{background:var(--green-dark);color:#fff}
  .contact__text{position:absolute;left:14px;top:12px;font-size:7.6px;line-height:1.35}
  .contact__text h2{font-size:11px;font-weight:700;margin-bottom:3px}
  .contact__hill{position:absolute;left:0;top:92px;width:195px;height:170px}
  .middle{background:var(--lime)}
  .cover{background:var(--lime)}
  .cover__title{position:absolute;top:22px;left:0;width:100%;text-align:center;font-family:"Cinzel",Georgia,serif;font-size:20px;color:var(--ink);letter-spacing:.5px;z-index:2}
  .cover__place{position:absolute;right:12px;top:335px;color:#fff;font-size:11px;line-height:1.35;text-align:center;z-index:2}

  /* inside */
  .inside-1{background:var(--lime)}
  .inside-2,.inside-3{background:var(--lime)}
  .wave{position:absolute;left:0;width:100%}
  .features{position:absolute;left:14px;top:146px;font-size:8px;line-height:1.35;z-index:2}
  .features h3{font-size:10px;font-weight:700;line-height:1.1;margin-bottom:4px}
  .features ul{list-style:none;margin:0 0 8px 8px}
  .features p{margin-bottom:5px}
  .prices{position:absolute;left:209px;top:286px;width:360px;font-size:7.6px;line-height:1.3;z-index:2}
  .prices h3{font-size:10px;font-weight:700;margin-bottom:4px}
  .price-row{display:flex;align-items:baseline}
  .price-row__label{white-space:nowrap}
  .price-row__dash{flex:1;border-bottom:1px dashed var(--ink);margin:0 3px;transform:translateY(-2px)}
  .price-row__value{white-space:nowrap;width:130px}
  .prices__note{margin-top:10px}
  .stand{position:absolute;left:435px;bottom:16px;font-size:7.6px;z-index:2}
</style>
</head>
<body>

<!-- Outside -->
<section class="sheet sheet--outside">
  <div class="panel contact">
    <div class="contact__text">
      <h2>Kontaktdaten:</h2>
      Kerstin Wallbach und Tobias Quast<br>
      Oberhain 7<br>
      98634 Waldbrunn/OT Oberhain<br>
      0172/4830295<br>
      toblerquast69@postfach.de
    </div>
    <svg class="contact__hill" viewBox="0 0 195 170" role="img" aria-label="Radfahrer-Silhouette auf grünem Hügel">
      <path d="M0 40 C60 -10 150 0 195 30 L195 170 L0 170 Z" fill="var(--lime-light)"/>
      <path d="M0 170 C70 160 150 110 195 60 L195 170 Z" fill="var(--green-dark)"/>
    </svg>
    <div class="photo photo--village" style="left:0;top:262px;width:195px;height:156px" role="img" aria-label="Luftbild des Ferienhauses im herbstlichen Tal"></div>
  </div>
  <div class="panel middle">
    <div class="photo photo--landscape" style="left:0;top:12px;width:195px;height:298px" role="img" aria-label="Luftbild von Dorf und Hügeln im Herbst"></div>
    <svg style="position:absolute;left:0;top:0" width="195" height="418" viewBox="0 0 195 418">
      <rect x="0" y="0" width="195" height="12" fill="var(--green-dark)"/>
      <path d="M0 190 L80 310 L195 310 L195 418 L0 418 Z" fill="var(--lime)"/>
    </svg>
  </div>
  <div class="panel cover">
    <div class="photo photo--landscape" style="left:0;top:12px;width:195px;height:302px" role="img" aria-label="Luftbild des Ferienhauses mit Landstraße und Herbstwald"></div>
    <svg style="position:absolute;left:0;top:0" width="195" height="418" viewBox="0 0 195 418">
      <rect x="0" y="0" width="195" height="12" fill="var(--green-dark)"/>
      <path d="M0 314 L195 314 L195 418 L0 418 Z" fill="var(--lime)"/>
      <path d="M65 314 L195 314 L195 418 L130 418 C110 380 90 340 65 314 Z" fill="var(--green-dark)"/>
    </svg>
    <div class="photo" style="left:12px;top:326px;width:86px;height:80px;background:var(--green-mid);border-radius:40% 40% 10% 10%;opacity:.8" role="img" aria-label="Radfahrer-Silhouette"></div>
    <h1 class="cover__title">Ferienhaus</h1>
    <p class="cover__place">Waldbrunn<br>OT Oberhain</p>
  </div>
</section>

<!-- Inside -->
<section class="sheet sheet--inside">
  <svg style="position:absolute;left:0;top:0" width="585" height="418" viewBox="0 0 585 418">
    <path d="M0 115 C60 100 140 120 195 150 L195 418 L0 418 Z" fill="var(--pale)"/>
    <path d="M195 300 C280 270 420 250 585 270 L585 418 L195 418 Z" fill="var(--pale)"/>
    <path d="M0 270 C70 250 140 270 195 290 L195 418 L0 418 Z" fill="var(--lime-light)" opacity=".55"/>
  </svg>
  <div class="panel inside-1">
    <div class="photo photo--village framed" style="left:12px;top:14px;width:170px;height:110px" role="img" aria-label="Luftbild des Hofes mit Wiesen"></div>
    <div class="features">
      <h3>Nichtraucherwohnung<br>bestehend aus</h3>
      <ul><li>1 Schlafzimmer</li><li>Wohnzimmer/Küche</li><li>Badezimmer</li></ul>
      <p>für bis zu 4 Personen<br>Terrasse und Parkplatz direkt<br>am Ferienhaus</p>
      <p>Hunde willkommen</p>
    </div>
    <div class="photo photo--bath framed" style="left:12px;top:300px;width:84px;height:98px" role="img" aria-label="Dusche und WC im Badezimmer"></div>
    <div class="photo photo--bath framed" style="left:100px;top:300px;width:84px;height:98px" role="img" aria-label="Waschtisch und Tür im Badezimmer"></div>
    <p class="caption" style="top:402px">Badezimmer</p>
  </div>
  <div class="panel inside-2">
    <div class="photo photo--room framed" style="left:12px;top:14px;width:170px;height:120px" role="img" aria-label="Wohnzimmer mit Holzboden und Essplatz"></div>
    <p class="caption" style="top:137px">Wohnzimmer/Küche</p>
    <div class="photo photo--room framed" style="left:12px;top:152px;width:170px;height:120px" role="img" aria-label="Küchenzeile und Treppe"></div>
  </div>
  <div class="panel inside-3">
    <div class="photo photo--room framed" style="left:12px;top:14px;width:170px;height:120px" role="img" aria-label="Schlafzimmer im Dachgeschoss mit Holzbalken"></div>
    <p class="caption" style="top:137px">Schlafzimmer</p>
    <div class="photo photo--room framed" style="left:12px;top:152px;width:170px;height:120px" role="img" aria-label="Tagesbett im Schlafzimmer"></div>
  </div>
  <div class="prices">
    <h3>Preise:</h3>
    <div class="price-row"><span class="price-row__label">für 2 Pers.</span><span class="price-row__dash"></span><span class="price-row__value">86€ pro Übernachtung</span></div>
    <div class="price-row"><span class="price-row__label">ab 4 Übernachtungen</span><span class="price-row__dash"></span><span class="price-row__value">76€ pro Übernachtung</span></div>
    <div class="price-row"><span class="price-row__label">zzgl. für die 3 und 4 Person</span><span class="price-row__dash"></span><span class="price-row__value">22€ je Person und Übernachtung</span></div>
    <div class="price-row"><span class="price-row__label">Pro Hund und Übernachtung</span><span class="price-row__dash"></span><span class="price-row__value">5€&nbsp;&nbsp; pro Hund und Übernachtung</span></div>
    <p class="prices__note">Mindestaufenthalt<br>2 Übernachtungen<br>Preise verstehen sich inkl.<br>aller Nebenkosten</p>
  </div>
  <p class="stand">Stand Okt . 2020)</p>
</section>

</body>
</html>
```